business card for Franco-Turkish restaurant

We are a Franco-Turkish restaurant, Le Mirandel, based in the Cotes d'Armor in Brittany, near the Pink Granite Coast. We serve mainly Turkish cuisine. We would like a card reminding Britain and Turkey. No flag. Color: turquoise (sea ..), green, red. There should be a space for 3 lines: name, address, phone / email

Industry/Entity Type

Fast Food Restaurant

Contact Information for Business Card

Dalbayrak Emrul
Addresse: 14 Rue Paul-Henri Duvic, 22450 Kervalhec, France
Tel:+33 2 96 47 08 39

Colors
33a6d7
f04a50
acd036

Requirements
Nice to have
• Symbols of Britain and Turkey
Should not have
• No flags

```html
<!DOCTYPE html>
<html lang="fr">
<head>
<meta charset="utf-8">
<title>Le Mirandel – carte de visite</title>
<link rel="stylesheet" href="https://fonts.googleapis.com/css2?family=Alegreya:wght@700;800&family=Open+Sans:wght@400;500&display=swap">
<style>
  :root {
    --page-bg: #ece8e2;
    --card-top: #ffffff;
    --card-bottom: #dcecf6;
    --turquoise: #33a6d7;
    --turquoise-deep: #1f86bd;
    --turquoise-light: #62bde4;
    --green: #acd036;
    --red: #f04a50;
    --ink-teal: #0f6482;
    --white: #ffffff;
  }
  * { box-sizing: border-box; margin: 0; padding: 0; }
  html, body {
    width: 1200px; height: 832px; overflow: hidden;
    background: var(--page-bg);
  }
  .card {
    position: absolute; left: 100px; top: 128px;
    width: 1000px; height: 575px; overflow: hidden;
    background: linear-gradient(180deg, var(--card-top) 0%, var(--card-bottom) 100%);
    box-shadow: 0 6px 24px rgba(0,0,0,.15);
  }
  .card__waves { position: absolute; inset: 0; }
  .brand-dot {
    position: absolute; left: 90px; top: 58px;
    width: 96px; height: 96px; border-radius: 50%;
    background: var(--red);
  }
  .tagline {
    position: absolute; left: 600px; top: 72px; width: 260px;
    text-align: center;
    font-family: "Alegreya", serif; font-weight: 700;
    font-size: 38px; line-height: 48px;
    color: var(--turquoise-deep);
  }
  .brand-name {
    position: absolute; left: 180px; top: 196px; width: 720px;
    text-align: center;
    font-family: "Alegreya", serif; font-weight: 800;
    font-size: 104px; line-height: 120px;
    color: var(--turquoise-deep);
  }
  .contact {
    position: absolute; left: 0; top: 385px; width: 100%;
    font-family: "Open Sans", sans-serif;
  }
  .contact__name {
    padding-left: 52px;
    font-size: 36px; font-weight: 500; line-height: 52px;
    color: var(--ink-teal);
  }
  .contact__line {
    display: flex; align-items: center; gap: 20px;
    padding-left: 50px; height: 58px;
    font-size: 28px; color: var(--white);
  }
  .contact__line svg { width: 30px; height: 30px; flex: none; }
</style>
</head>
<body>
  <div class="card">
    <svg class="card__waves" viewBox="0 0 1000 575" preserveAspectRatio="none" aria-hidden="true">
      <path d="M0 372 C 230 392, 560 350, 760 300 C 880 270, 960 240, 1000 222 L1000 575 L0 575 Z" fill="var(--turquoise)"/>
      <rect x="0" y="495" width="1000" height="80" fill="var(--turquoise-light)"/>
      <path d="M520 372 C 700 350, 870 300, 1000 205 L1000 228 C 880 300, 700 355, 520 372 Z" fill="var(--green)"/>
    </svg>

    <div class="brand-dot"></div>

    <p class="tagline">restaurant<br>franco-turque</p>

    <h1 class="brand-name">Le Mirandel</h1>

    <div class="contact">
      <p class="contact__name">Dalbayrak Emrul</p>
      <p class="contact__line">
        <svg viewBox="0 0 24 24"><path fill="var(--ink-teal)" d="M12 2a7 7 0 0 0-7 7c0 5 7 13 7 13s7-8 7-13a7 7 0 0 0-7-7zm0 9.5A2.5 2.5 0 1 1 12 6.5a2.5 2.5 0 0 1 0 5z"/></svg>
        14 Rue Paul-Henri Duvic, 22450 Kervalhec, France
      </p>
      <p class="contact__line">
        <svg viewBox="0 0 24 24"><circle cx="12" cy="12" r="10.5" fill="none" stroke="var(--ink-teal)" stroke-width="2"/><path fill="var(--ink-teal)" d="M8.6 6.5l1.6-.3 1 2.4-1.1 1c.6 1.3 1.5 2.2 2.7 2.8l1-1.1 2.4 1-.3 1.6c-.2.6-.8 1-1.5.9-3.6-.5-6.5-3.4-7-7-.1-.6.3-1.2.9-1.4z"/></svg>
        +33 2 96 47 08 39
      </p>
    </div>
  </div>
</body>
</html>
```